Course flyer - evolutive design

We want to have a nice design for our course programm.
In fact we are school language, and our course programm change approximatively each 2 weeks§.
For that we need a design that we can modify each 2 weeks (only dates change ) by ourselves.
We used to have a classical design but we want to upgrade it with a modern and attractive design.
We can have 3 versions one for each city.
We have 3 offices: Tunis, Sousse & Sfax
Attached you can find old designs

Target Market(s)

students from 16 years old till retired people 76 years old

Industry/Entity Type

Education

Font styles to use
Sans Serif

Requirements
Must have
• clear timing for courses (date, days, timing)
• prices
• Adresse (each flyer has its own adress)
• phone Number
• Cool image
Should not have
• Racism
• Violence
• Too much stuff

```html
<!DOCTYPE html>
<html lang="fr">
<head>
<meta charset="utf-8">
<title>Cours d'allemand – Mai/Juin 2016 – Tunis</title>
<link href="https://fonts.googleapis.com/css2?family=Oswald:wght@500;700&family=Roboto+Condensed:wght@400;700&display=swap" rel="stylesheet">
<style>
  :root{
    --maroon:#5a1b18;
    --maroon-dark:#461411;
    --red:#c8202a;
    --gold:#f2c318;
    --white:#ffffff;
    --grey:#5f5f5f;
  }
  *{margin:0;padding:0;box-sizing:border-box}
  html,body{width:847px;height:1200px;overflow:hidden;background:var(--white)}
  .flyer{position:relative;width:847px;height:1200px;overflow:hidden;background:var(--white);font-family:"Roboto Condensed",Arial,sans-serif;color:var(--white)}

  .flag{position:absolute;left:-40px;top:-60px;width:980px;height:420px;transform:rotate(-9deg);transform-origin:center;
    background:linear-gradient(180deg,rgba(22,22,22,.85) 0 30%,rgba(200,32,42,.85) 36% 62%,rgba(242,195,24,.85) 68% 100%);
    filter:blur(2px);opacity:.9}
  .flag-fade{position:absolute;left:0;top:0;width:847px;height:420px;background:linear-gradient(90deg,rgba(255,255,255,0) 0%,rgba(255,255,255,.55) 55%,rgba(255,255,255,.25) 100%)}

  .backdrop-right{position:absolute;left:0;top:380px;width:847px;height:820px;background:var(--maroon)}
  .backdrop-left{position:absolute;left:0;top:200px;width:418px;height:1000px;background:var(--maroon)}

  .brand{position:absolute;left:24px;top:40px;display:flex;align-items:center;gap:12px;padding:10px 18px;background:rgba(255,255,255,.9)}
  .brand-mark{width:22px;height:22px;border-radius:50%;background:var(--grey)}
  .brand-name{font-family:"Oswald",sans-serif;font-weight:700;font-size:32px;line-height:1;color:var(--grey)}

  .edition{position:absolute;right:22px;top:14px;font-family:"Oswald",sans-serif;font-weight:700;color:var(--red);text-align:right;line-height:1;font-size:26px}

  .title{position:absolute;left:470px;top:168px;font-family:"Oswald",sans-serif;font-weight:700;color:var(--red);text-align:right;width:300px;line-height:1;text-transform:uppercase}
  .title .l1{display:block;font-size:66px}
  .title .l2{display:block;font-size:62px}

  .photo-students{position:absolute;left:423px;top:395px;width:300px;height:270px;background:linear-gradient(160deg,#e9d9c4 0%,#c9a57e 45%,#6d5a45 100%)}
  .photo-woman{position:absolute;left:672px;top:720px;width:165px;height:480px;border-radius:70px 70px 0 0;background:linear-gradient(180deg,#d9b48e 0%,#f1eee8 35%,#7ea3c4 70%,#3d5c82 100%)}

  .schedule{position:absolute;top:226px;width:180px;font-size:17px;line-height:24px}
  .col-a{left:24px}
  .col-b{left:222px}
  .block{margin-bottom:24px}
  .type{font-family:"Oswald",sans-serif;font-weight:700;font-size:21px;line-height:26px;letter-spacing:.5px}
  .days{font-weight:700;font-size:16px;line-height:20px;margin-bottom:4px}
  .dates{font-family:"Oswald",sans-serif;font-weight:700;color:var(--gold);font-size:20px;line-height:28px}
  .slot{font-weight:700;border-bottom:1px solid rgba(255,255,255,.45);display:inline-block;margin:4px 0 6px;font-size:17px}
  .course{display:flex;gap:8px;font-weight:700}
  .course .lvl{color:var(--gold);width:38px}
  .subgroup{margin-top:12px}
  .new{display:inline-block;background:var(--gold);color:var(--maroon-dark);font-family:"Oswald",sans-serif;font-weight:700;font-size:17px;line-height:21px;padding:4px 8px;margin:4px 0;text-transform:uppercase}
  .biz{font-family:"Oswald",sans-serif;font-weight:700;color:var(--gold);font-size:18px;line-height:26px}

  .info{position:absolute;left:432px;top:722px;width:232px;font-size:15.5px;line-height:19px}
  .info ul{list-style:none}
  .info li{position:relative;padding-left:14px;margin-bottom:6px;font-weight:700}
  .info li::before{content:"";position:absolute;left:2px;top:7px;width:5px;height:5px;border-radius:50%;background:var(--white)}
  .price{color:var(--gold);font-weight:700;margin-top:6px}

  .office{position:absolute;left:432px;top:935px;width:232px}
  .city{font-family:"Oswald",sans-serif;font-weight:700;font-size:60px;line-height:1}
  .address{margin-top:8px;font-size:13px;line-height:16px;font-style:normal}

  .social{position:absolute;left:500px;top:1160px;font-size:13px;font-weight:700;display:flex;align-items:center;gap:6px}
  .social .dot{width:12px;height:12px;border-radius:50%;background:var(--white)}
</style>
</head>
<body>
<main class="flyer">
  <div class="flag" role="img" aria-label="German flag waving across the top of the flyer"></div>
  <div class="flag-fade"></div>
  <div class="backdrop-right"></div>
  <div class="backdrop-left"></div>

  <div class="brand">
    <span class="brand-mark"></span>
    <span class="brand-name">Verbalis group</span>
  </div>

  <div class="edition">MAI | JUIN 2016</div>

  <h1 class="title"><span class="l1">Cours</span><span class="l2">d'allemand</span></h1>

  <div class="photo-students" role="img" aria-label="Photo of two smiling students studying with a laptop and books"></div>
  <div class="photo-woman" role="img" aria-label="Photo of a young woman standing with a bag and books"></div>

  <section class="schedule col-a">
    <div class="block">
      <div class="type">INTENSIF</div>
      <div class="days">(Lundi - Vendredi)</div>
      <div class="dates">07/03 - 25/03</div>
      <div class="slot">09H30 - 12H30</div>
      <div class="course"><span class="lvl">A1.1</span><span>DK2090</span></div>
      <div class="course"><span class="lvl">A1.2</span><span>DK2091</span></div>
      <div class="course"><span class="lvl">A2.1</span><span>DK2092</span></div>
      <div class="course"><span class="lvl">A2.2</span><span>DK2093</span></div>
      <div class="course"><span class="lvl">B1.1</span><span>DK2094</span></div>
      <div class="subgroup">
        <div class="slot">13H00 - 16H00</div>
        <div class="course"><span class="lvl">A1.1</span><span>DK2095</span></div>
        <div class="course"><span class="lvl">A1.2</span><span>DK2096</span></div>
        <div class="course"><span class="lvl">A2.1</span><span>DK2097</span></div>
        <div class="course"><span class="lvl">A2.2</span><span>DK2098</span></div>
        <div class="course"><span class="lvl">B1.1</span><span>DK2099</span></div>
      </div>
    </div>
    <div class="block">
      <div class="type">INTENSIF</div>
      <div class="days">(Lundi - Vendredi)</div>
      <div class="dates">28/03 - 15/04</div>
      <div class="slot">09H30 - 12H30</div>
      <div class="course"><span class="lvl">A1.1</span><span>DK2105</span></div>
      <div class="course"><span class="lvl">A1.1</span><span>DK2106</span></div>
      <div class="course"><span class="lvl">A1.2</span><span>DK2107</span></div>
      <div class="course"><span class="lvl">A2.1</span><span>DK2108</span></div>
      <div class="course"><span class="lvl">A2.2</span><span>DK2109</span></div>
      <div class="subgroup">
        <div class="slot">13H00 - 16H00</div>
        <div class="course"><span class="lvl">A1.1</span><span>DK2110</span></div>
        <div class="course"><span class="lvl">A1.1</span><span>DK2111</span></div>
        <div class="course"><span class="lvl">A1.2</span><span>DK2112</span></div>
        <div class="course"><span class="lvl">A2.1</span><span>DK2113</span></div>
        <div class="course"><span class="lvl">C1.1</span><span>DK2114</span></div>
      </div>
    </div>
  </section>

  <section class="schedule col-b">
    <div class="block">
      <div class="type">EXTENSIF</div>
      <div class="days">(Lun / Mer / Ven)</div>
      <div class="dates">29/02 - 25/03</div>
      <div class="slot">18H30 - 21H30</div>
      <div class="course"><span class="lvl">A1.1</span><span>DK2101</span></div>
      <div class="course"><span class="lvl">A1.2</span><span>DK2102</span></div>
      <div class="course"><span class="lvl">A2.1</span><span>DK2103</span></div>
      <div class="new">Nouveau cours :<br>Business-Deutsch</div>
      <div class="course"><span class="lvl">A1.1</span><span>DK2104</span></div>
    </div>
    <div class="block">
      <div class="dates">28/03 - 22/04</div>
      <div class="course"><span class="lvl">A1.1</span><span>DK2121</span></div>
      <div class="course"><span class="lvl">A1.2</span><span>DK2122</span></div>
      <div class="course"><span class="lvl">A2.1</span><span>DK2123</span></div>
      <div class="course"><span class="lvl">A2.2</span><span>DK2124</span></div>
      <div class="biz">BUSINESS-DEUTSCH</div>
      <div class="course"><span class="lvl">A1.1</span><span>DK2125</span></div>
      <div class="course"><span class="lvl">A1.2</span><span>DK2126</span></div>
    </div>
    <div class="block">
      <div class="type">EXTENSIF</div>
      <div class="days">(Mardi / Jeudi)</div>
      <div class="dates">29/03 - 05/05</div>
      <div class="slot">18H30 - 21H30</div>
      <div class="course"><span class="lvl">A1.1</span><span>DK2115</span></div>
      <div class="course"><span class="lvl">A1.1</span><span>DK2116</span></div>
      <div class="course"><span class="lvl">A2.1</span><span>DK2117</span></div>
      <div class="course"><span class="lvl">A2.2</span><span>DK2118</span></div>
      <div class="course"><span class="lvl">B1.1</span><span>DK2119</span></div>
      <div class="course"><span class="lvl">B1.2</span><span>DK2120</span></div>
    </div>
  </section>

  <section class="info">
    <ul>
      <li>Toute inscription doit impérativement se faire au plus tard une semaine avant le début des cours.</li>
      <li>Nombre minimum de 4 participants requis.</li>
      <li>L'horaire des cours est susceptible d'être modifié.</li>
    </ul>
    <p class="price">Prix par module 340 TND.</p>
  </section>

  <section class="office">
    <div class="city">TUNIS</div>
    <address class="address">
      Imm. Les Palmiers, 2ème étage<br>
      8 Rue de l'Énergie Solaire<br>
      1082 Centre Urbain Nord<br>
      Tel : +216 71 000 482<br>
      Email : tunis@verbalis-langues.tn<br>
      Web : www.verbalis-langues.tn
    </address>
  </section>

  <div class="social"><span class="dot"></span><span>www.facebook.com/verbalislangues</span></div>
</main>
</body>
</html>
```